Fitness competition business needs a card design

I need a professional business card design using my logo. The card will be horizontal with rounded edges.

Target Market(s)

Female fitness competitors

Industry/Entity Type

Fitness

Contact Information for Business Card

Rose-Lynn Darby
Owner
stagevarno.com
555.301.2187
info@stagevarno.com

Font styles to use
Serif

Colors

Designer to choose colors to be used in the design.

Requirements
Must have
• On the back please add the following:
• Figure
• Bikini
• Physique
• Fitness
Nice to have
• Looking for a very sleek design, contemporary and easy to read.
Should not have
• Should not be difficult to read or be too busy

```html
<!DOCTYPE html>
<html lang="en">
<head>
<meta charset="utf-8">
<title>Stage Varno — Business Card</title>
<link href="https://fonts.googleapis.com/css2?family=Open+Sans:wght@400;600&family=Oswald:wght@600&display=swap" rel="stylesheet">
<style>
  :root {
    --bg: #e9e6e1;
    --card-white: #f7f7f7;
    --card-dark: #4a4a4c;
    --card-dark-edge: #3c3c3e;
    --ink: #3a3a3a;
    --ink-soft: #6b6b6b;
    --red: #d7262c;
    --white: #ffffff;
  }
  * { box-sizing: border-box; margin: 0; padding: 0; }
  html, body { width: 773px; height: 1200px; overflow: hidden; }
  body {
    background: var(--bg);
    font-family: "Open Sans", Arial, sans-serif;
    display: flex;
    flex-direction: column;
    align-items: center;
    justify-content: center;
    gap: 90px;
  }
  .card {
    width: 660px;
    height: 377px;
    border-radius: 26px;
    position: relative;
    box-shadow: 0 10px 28px rgba(0,0,0,0.18);
  }
  .card--front { background: var(--card-white); }
  .card--back {
    background: linear-gradient(160deg, var(--card-dark) 0%, var(--card-dark-edge) 100%);
    display: flex;
    flex-direction: column;
    align-items: center;
    justify-content: center;
    gap: 22px;
  }

  .holder { position: absolute; left: 52px; top: 120px; }
  .holder__name { font-size: 26px; font-weight: 400; color: var(--ink); letter-spacing: 0.2px; }
  .holder__rule { width: 230px; height: 2px; background: var(--red); margin: 10px 0 6px; }
  .holder__title { font-size: 13px; color: var(--red); }

  .contact { position: absolute; left: 52px; top: 215px; list-style: none; }
  .contact__item {
    display: flex; align-items: center; gap: 10px;
    font-size: 13px; color: var(--ink-soft); margin-bottom: 10px;
  }
  .contact__item--web { color: var(--red); margin-top: 14px; }
  .contact__icon { width: 14px; height: 14px; flex: none; }

  .brand { display: flex; align-items: center; gap: 12px; }
  .brand__mark { width: 18px; height: 18px; background: var(--red); }
  .brand__name {
    font-family: "Oswald", Arial, sans-serif;
    font-weight: 600;
    font-size: 40px;
    letter-spacing: 1px;
    text-transform: uppercase;
    line-height: 1;
  }
  .card--front .brand { position: absolute; right: 48px; top: 100px; }
  .card--front .brand__name { color: var(--red); }
  .card--back .brand__name { color: var(--white); font-size: 56px; }
  .card--back .brand__mark { width: 24px; height: 24px; }

  .divisions {
    display: flex; gap: 14px; list-style: none;
    font-size: 15px; color: var(--white); letter-spacing: 0.5px;
  }
  .divisions li + li::before { content: "|"; color: var(--red); margin-right: 14px; }
</style>
</head>
<body>

  <section class="card card--front" aria-label="Card front">
    <div class="holder">
      <p class="holder__name">Rose-Lynn Darby</p>
      <div class="holder__rule"></div>
      <p class="holder__title">Owner</p>
    </div>
    <ul class="contact">
      <li class="contact__item">
        <svg class="contact__icon" viewBox="0 0 24 24" aria-hidden="true"><path fill="#d7262c" d="M6.6 10.8a15.1 15.1 0 0 0 6.6 6.6l2.2-2.2c.3-.3.7-.4 1-.2 1.1.4 2.3.6 3.6.6.6 0 1 .4 1 1V20c0 .6-.4 1-1 1A17 17 0 0 1 3 4c0-.6.4-1 1-1h3.5c.6 0 1 .4 1 1 0 1.3.2 2.5.6 3.6.1.3 0 .7-.2 1z"/></svg>
        555.301.2187
      </li>
      <li class="contact__item">
        <svg class="contact__icon" viewBox="0 0 24 24" aria-hidden="true"><rect x="2" y="5" width="20" height="14" rx="2" fill="#d7262c"/><path d="M3 6l9 7 9-7" stroke="#fff" stroke-width="1.6" fill="none"/></svg>
        info@stagevarno.com
      </li>
      <li class="contact__item contact__item--web">
        <svg class="contact__icon" viewBox="0 0 24 24" aria-hidden="true"><circle cx="12" cy="12" r="9" fill="none" stroke="#d7262c" stroke-width="2"/><path d="M3 12h18M12 3c3 3 3 15 0 18M12 3c-3 3-3 15 0 18" stroke="#d7262c" stroke-width="1.5" fill="none"/></svg>
        stagevarno.com
      </li>
    </ul>
    <div class="brand">
      <span class="brand__mark" aria-hidden="true"></span>
      <span class="brand__name">Stage Varno</span>
    </div>
  </section>

  <section class="card card--back" aria-label="Card back">
    <div class="brand">
      <span class="brand__mark" aria-hidden="true"></span>
      <span class="brand__name">Stage Varno</span>
    </div>
    <ul class="divisions">
      <li>Figure</li>
      <li>Bikini</li>
      <li>Physique</li>
      <li>Fitness</li>
    </ul>
  </section>

</body>
</html>
```